Hot young IT advisor needs business cards as upscale and innovative as they are

We need business cards that make a statement about who we are, as a young and upscale IT advisor. Our whole angle is innovation and tenacity in our personal relationships with our clients. We've just done a brand overhaul and need cards that have the new logos, but we're also looking for someone with a sixth sense who can capture what sets us apart and communicate that with a business card. Clean, minimalist, upscale, innovative, personal. Our budget only allows room for them to be soft-touch, no spot gloss or foil designs please.

Target Market(s)

High-level decision makers at middle-market and large organizations in the healthcare, financial services, sports and entertainment, K-12 education, college and university, state and local government, and federal government sectors.

Industry/Entity Type

Information Technology

Font styles to use
Sans Serif

Colors
ec1f27
606060
ffffff

Requirements
Should not have
• Designs with low contrast which would require spot-gloss or embossing.

```html
<!DOCTYPE html>
<html lang="en">
<head>
<meta charset="utf-8">
<title>Norvale Business Card</title>
<link href="https://fonts.googleapis.com/css2?family=Lato:wght@400;700&display=swap" rel="stylesheet">
<style>
  :root {
    --brand-red: #ec1f27;
    --ink: #2f3330;
    --text-grey: #4a4a4a;
    --rule-grey: #9a9a9a;
    --rule-light: #dcdcdc;
    --paper: #ffffff;
    --backdrop: #7b7b7b;
    --charcoal: #363a36;
  }
  * { margin: 0; padding: 0; box-sizing: border-box; }
  html, body { width: 1200px; height: 1200px; overflow: hidden; }
  body {
    background: var(--backdrop);
    font-family: "Lato", sans-serif;
    position: relative;
  }
  .card {
    position: absolute;
    top: 310px;
    height: 594px;
    box-shadow: 2px 3px 4px rgba(0,0,0,0.35);
  }
  .card-front { left: 234px; width: 364px; background: var(--paper); }
  .card-back { left: 627px; width: 370px; }
  .card-back .brand-field {
    width: 100%; height: 100%; display: block;
    background: linear-gradient(100deg, var(--charcoal) 0%, var(--charcoal) 30%, var(--brand-red) 60%, var(--brand-red) 100%);
  }
  .centered { position: absolute; left: 0; width: 100%; text-align: center; }
  .company-name {
    top: 214px;
    font-size: 30px; font-weight: 400; letter-spacing: 1px;
    color: var(--ink);
  }
  .person-name {
    top: 341px; font-size: 21px; font-weight: 700; color: var(--ink); letter-spacing: 0.3px;
  }
  .person-name .surname { color: var(--brand-red); }
  .person-role { top: 365px; font-size: 17px; color: var(--text-grey); }
  .contact-rule { position: absolute; top: 407px; left: 87px; width: 190px; height: 1px; background: var(--rule-grey); }
  .contact-icons { position: absolute; top: 396px; left: 141px; width: 82px; height: 24px; }
  .contact-list { top: 431px; font-size: 16.5px; line-height: 22px; color: var(--text-grey); }
  .address-rule { position: absolute; top: 507px; left: 88px; width: 194px; height: 1px; background: var(--rule-light); }
  .address { top: 517px; font-size: 16.5px; line-height: 22px; color: var(--text-grey); }
</style>
</head>
<body>
  <section class="card card-front">
    <div class="centered company-name">NORVALE</div>
    <div class="centered person-name">MARCUS <span class="surname">HALE</span></div>
    <div class="centered person-role">Managing Director</div>
    <div class="contact-rule"></div>
    <svg class="contact-icons" viewBox="0 0 82 24" aria-hidden="true">
      <rect x="0" y="11" width="82" height="2" fill="#ffffff"/>
      <circle cx="12" cy="12" r="12" fill="#ec1f27"/>
      <path d="M6 10 q6 -5 12 0 l-2 2 h-2 l-1 -2 h-2 l-1 2 h-2z M8 13 h8 v4 h-8z" fill="#fff"/>
      <circle cx="39" cy="12" r="12" fill="#ec1f27"/>
      <rect x="32" y="7" width="14" height="10" fill="#fff"/>
      <path d="M32 7 l7 6 l7 -6" stroke="#ec1f27" stroke-width="1.5" fill="none"/>
      <circle cx="66" cy="12" r="12" fill="#ec1f27"/>
      <circle cx="66" cy="12" r="6.5" fill="#fff"/>
      <path d="M59.5 12 h13 M66 5.5 q-4 6.5 0 13 M66 5.5 q4 6.5 0 13" stroke="#ec1f27" stroke-width="1.2" fill="none"/>
    </svg>
    <div class="centered contact-list">
      <div class="phone">044-555 010 234</div>
      <div class="email">hello@norvale.com</div>
      <div class="website">www.norvale.com</div>
    </div>
    <div class="address-rule"></div>
    <div class="centered address">
      <div>88, Linden Court Road,</div>
      <div>30817,Northbridge</div>
    </div>
  </section>
  <section class="card card-back">
    <div class="brand-field" role="img" aria-label="Large brand symbol decoration in charcoal and red with white dotted data trail"></div>
  </section>
</body>
</html>
```